Bright Leaf Bistro & Pantry Squarespace Website Files

We need a Squarespace website for a new company called "Bright Leaf Bistro & Pantry".

The company is committed to providing the highest quality, fresh and natural food, health and wellness products.

We would like to see designs that use the colors of our logo. Please provide graphic design and layout for the site.

The final design should communicate health and wellness.

Target Market(s)

Bright Leaf Bistro & Pantry is a new company that will offer customers organic and
locally grown produce, chemical and preservative-free groceries, cruelty-free body care and eco-household products. Additionally, our kitchen will offer healthy lunch and dinner options emphasizing organic and whole food options, recognizing the trend within the restaurant industry for the demand for healthy cuisine. The restaurant will procure local foods when possible, reducing dependence on fossil fuels used for transportation. All of our products are healthy alternatives to the products available at conventional grocery chains.

Located in the heart of the growing Harlow Street section of Lewiston, NY, the
marketplace will serve a community of residents in Lewiston, residents in
Niagara Falls, and residents in Niagara Falls, Ontario, Canada.

The creation of the marketplace is in response to the growing demand in the community for a local natural food store.

Industry/Entity Type

Cafe

Font styles to use
Sans Serif

Colors
00a990
faa54b
87cfc7
f37122

Requirements
Must have
• Home page, Events, Cafe Menu, Marketplace Products, Health Info, News, Recipes, Contact Us (Email form and Social Media links), Newsletter sign up.
Nice to have
• Order Online
Should not have
• (Can't think of anything right now :-)

```html
<!DOCTYPE html>
<html lang="en">
<head>
<meta charset="utf-8">
<title>Bright Leaf Bistro &amp; Pantry</title>
<link href="https://fonts.googleapis.com/css2?family=Ubuntu:wght@300;400;500;700&display=swap" rel="stylesheet">
<style>
:root{
  --teal:#1a9d86;
  --teal-dark:#138a75;
  --teal-light:#87cfc7;
  --orange:#f0621f;
  --orange-light:#faa54b;
  --wood:#6b4a31;
  --wood-dark:#4e3422;
  --text:#555;
  --white:#fff;
}
*{margin:0;padding:0;box-sizing:border-box}
html,body{width:695px;height:1200px;overflow:hidden;background:var(--white)}
body{position:relative;font-family:'Ubuntu',sans-serif;color:var(--text)}
.abs{position:absolute}
.brand{left:65px;top:12px;font-size:17px;font-weight:500;color:var(--teal);display:flex;align-items:center;gap:6px}
.brand-dot{width:10px;height:10px;border-radius:50%;background:var(--orange)}
.phone{right:64px;top:21px;font-size:9px;color:var(--teal);display:flex;align-items:center;gap:4px}
.nav{left:65px;top:46px;width:567px;height:33px;background:var(--orange);display:flex;align-items:center}
.nav a{color:var(--white);font-size:8px;text-decoration:none;height:100%;display:flex;align-items:center;padding:0 9px;border-right:1px solid rgba(0,0,0,.12)}
.nav a.active{background:var(--teal);padding:0 15px}
.nav .signup{position:absolute;right:22px;top:10px;height:17px;background:var(--teal);border-radius:2px;font-size:8px;font-weight:500;padding:0 9px;border:none}
.wood{left:0;top:79px;width:695px;height:241px;background:linear-gradient(90deg,var(--wood-dark),var(--wood) 20%,#7a5639 50%,var(--wood) 80%,var(--wood-dark))}
.hero{left:65px;top:92px;width:566px;height:267px;background:linear-gradient(120deg,#7fae45 0%,#a8422f 35%,#5c2f4a 55%,#8fbf5a 80%,#d9e3c8 100%);box-shadow:0 8px 6px -4px rgba(0,0,0,.55)}
.hero-circle{left:425px;top:135px;width:186px;height:186px;border-radius:50%;background:rgba(26,157,134,.93);color:var(--white);text-align:center;padding-top:50px}
.hero-circle h1{font-size:26px;font-weight:400}
.hero-circle p{font-size:7.5px;line-height:12px;margin:6px 22px 0}
.btn-learn{left:478px;top:263px;width:80px;height:22px;background:var(--orange);color:var(--white);font-size:8px;font-weight:500;border-radius:3px;display:flex;align-items:center;justify-content:center}
.dots{left:331px;top:332px;display:flex;gap:4px}
.dots span{width:5px;height:5px;border-radius:50%;background:var(--white)}
.dots span:first-child{background:var(--orange)}
.section-title{font-size:18px;color:var(--teal);font-weight:400}
.products-title{left:0;width:695px;top:399px;text-align:center}
.arrow{top:403px}
.card{top:436px;width:131px}
.card .img{height:88px}
.card h3{font-size:8.5px;color:var(--orange);font-weight:400;margin-top:10px}
.card p{font-size:6.5px;line-height:12px;margin-top:6px}
.card .btns{display:flex;gap:4px;margin-top:5px}
.btn{height:15px;font-size:6.5px;color:var(--white);display:flex;align-items:center;justify-content:center}
.btn.green{background:var(--teal);width:48px}
.btn.orange{background:var(--orange-light);width:49px;background:#f58a3d}
.health{left:65px;top:632px;width:566px;height:112px;background:var(--orange);border-radius:4px}
.health .img{position:absolute;left:11px;top:15px;width:136px;height:82px;border-radius:3px;background:linear-gradient(135deg,#d8e4ec,#b3c4cf 50%,#e9b9a6)}
.health h2{position:absolute;left:163px;top:23px;font-size:18px;font-weight:400;color:var(--white)}
.health h2 span{color:#3a2a20}
.health p{position:absolute;left:164px;top:47px;width:380px;font-size:7.3px;line-height:12px;color:var(--white)}
.health .btn{position:absolute;left:164px;top:78px;width:49px;height:17px;background:var(--teal);font-weight:500}
.events-title{left:63px;top:768px}
.news-title{left:403px;top:768px}
.event-img{left:65px;top:800px;width:324px;height:168px;background:linear-gradient(160deg,#6e9a4a,#b9c98a 40%,#3f6f2e 70%,#c97a3a)}
.event-date{left:65px;top:922px;width:57px;height:46px;background:var(--orange);color:var(--white);padding:8px 0 0 8px}
.event-date b{display:block;font-size:14px;font-weight:400;line-height:14px}
.event-date small{font-size:7.5px}
.event-caption{left:122px;top:922px;width:267px;height:46px;background:rgba(26,140,90,.75);color:var(--white);font-size:8px;line-height:13px;padding:10px 10px 0 9px}
.rule{left:403px;width:228px;height:1px;background:#ddd}
.news-item{left:403px;width:228px}
.news-item .img{position:absolute;left:0;top:0;width:72px;height:59px}
.news-item h4{position:absolute;left:82px;top:0;font-size:8.3px;line-height:12px;color:var(--orange);font-weight:400}
.news-item p{position:absolute;left:82px;top:26px;font-size:6.6px;line-height:12px;color:#333}
.news-item p a{color:var(--teal);text-decoration:none}
.footer{left:0;top:1005px;width:695px;height:195px;background:var(--teal);color:var(--white)}
.footer ul{position:absolute;list-style:none;font-size:7.5px;line-height:15px}
.footer h5{position:absolute;left:461px;top:32px;font-size:11.5px;font-weight:400}
.footer .note{position:absolute;left:461px;top:57px;width:170px;font-size:6.6px;line-height:12px}
.footer .input{position:absolute;left:461px;top:85px;width:161px;height:18px;background:var(--teal-light);font-size:5.5px;padding:6px 6px;color:#eef}
.footer .subscribe{position:absolute;left:461px;top:111px;width:47px;height:16px;background:var(--orange);border-radius:3px;font-size:7px;font-weight:500;display:flex;align-items:center;justify-content:center}
.footer .copy{position:absolute;left:0;width:695px;top:175px;text-align:center;font-size:6.5px}
</style>
</head>
<body>
<div class="abs brand"><span class="brand-dot"></span>Bright Leaf Bistro &amp; Pantry</div>
<div class="abs phone">
  <svg width="9" height="9" viewBox="0 0 24 24"><path fill="#f0621f" d="M6.6 10.8a15 15 0 0 0 6.6 6.6l2.2-2.2c.3-.3.7-.4 1-.2 1.1.4 2.3.6 3.6.6.6 0 1 .4 1 1V20c0 .6-.4 1-1 1A17 17 0 0 1 3 4c0-.6.4-1 1-1h3.5c.6 0 1 .4 1 1 0 1.3.2 2.5.6 3.6.1.3 0 .7-.2 1z"/></svg>
  Call Now : 1-800-555-0142
</div>
<nav class="abs nav">
  <a class="active">Home</a><a>Events</a><a>Cafe Menu</a><a>Marketplace Products</a><a>Health Info</a><a>News</a><a>Recipes</a><a>Contact Us</a>
  <a class="signup">Newsletter Sign Up</a>
</nav>

<div class="abs wood" role="img" aria-label="Wooden plank background"></div>
<div class="abs hero" role="img" aria-label="Basket of fresh vegetables and grapes"></div>
<div class="abs hero-circle">
  <h1>Bright Leaf</h1>
  <p>Lorem Ipsum is simply dummy text of the printing and typesetting industry. Lorem Ipsum has been the industry's</p>
</div>
<div class="abs btn-learn">Learn More</div>
<div class="abs dots"><span></span><span></span><span></span><span></span></div>

<h2 class="abs section-title products-title">Our Products</h2>
<svg class="abs arrow" style="left:64px" width="10" height="14" viewBox="0 0 10 14"><path d="M8 1L2 7l6 6" fill="none" stroke="#999" stroke-width="2"/></svg>
<svg class="abs arrow" style="left:623px" width="10" height="14" viewBox="0 0 10 14"><path d="M2 1l6 6-6 6" fill="none" stroke="#999" stroke-width="2"/></svg>

<div class="abs card" style="left:65px">
  <div class="img" role="img" aria-label="Fresh vegetables on a wooden table" style="background:linear-gradient(135deg,#b8342a,#6b5a3e 50%,#d7dccd)"></div>
  <h3>Highest Quality</h3><p>Lorem Ipsum is simply dummy text of the printing and typesetting industry.</p>
  <div class="btns"><span class="btn green">Add To Cart</span><span class="btn orange">More Info</span></div>
</div>
<div class="abs card" style="left:209px">
  <div class="img" role="img" aria-label="Colourful bell peppers" style="background:linear-gradient(135deg,#4e8a2f,#e8c21a 45%,#c8321f)"></div>
  <h3>Highest Quality</h3><p>Lorem Ipsum is simply dummy text of the printing and typesetting industry.</p>
  <div class="btns"><span class="btn green">Add To Cart</span><span class="btn orange">More Info</span></div>
</div>
<div class="abs card" style="left:355px">
  <div class="img" role="img" aria-label="Essential oil bottles with flowers" style="background:linear-gradient(135deg,#e6dcea,#c9a6c8 50%,#8c6a55)"></div>
  <h3>Highest Quality</h3><p>Lorem Ipsum is simply dummy text of the printing and typesetting industry.</p>
  <div class="btns"><span class="btn green">Add To Cart</span><span class="btn orange">More Info</span></div>
</div>
<div class="abs card" style="left:500px">
  <div class="img" role="img" aria-label="Fresh blueberries with leaves" style="background:linear-gradient(135deg,#6e5a48,#2c3d6e 50%,#3e6a3a)"></div>
  <h3>Highest Quality</h3><p>Lorem Ipsum is simply dummy text of the printing and typesetting industry.</p>
  <div class="btns"><span class="btn green">Add To Cart</span><span class="btn orange">More Info</span></div>
</div>

<section class="abs health">
  <div class="img" role="img" aria-label="Hands holding a fitness tracker and smartphone"></div>
  <h2>Health <span>Info</span></h2>
  <p>Lorem Ipsum is simply dummy text of the printing and typesetting industry. Lorem Ipsum has been the industry's standard dummy text ever since the 1500s, when an unknown printer</p>
  <span class="btn">More Info</span>
</section>

<h2 class="abs section-title events-title">Events</h2>
<svg class="abs" style="left:375px;top:775px" width="16" height="10" viewBox="0 0 16 10"><path d="M5 1L1 5l4 4M11 1l4 4-4 4" fill="none" stroke="#888" stroke-width="1.6"/></svg>
<div class="abs event-img" role="img" aria-label="Crate of fresh vegetables and leafy greens"></div>
<div class="abs event-date"><b>APRIL</b><small>21th ,2015</small></div>
<div class="abs event-caption">Lorem Ipsum is simply dummy text of the printing and typeset-ting industry.</div>

<h2 class="abs section-title news-title">News</h2>
<svg class="abs" style="left:617px;top:775px" width="16" height="10" viewBox="0 0 16 10"><path d="M5 1L1 5l4 4M11 1l4 4-4 4" fill="none" stroke="#888" stroke-width="1.6"/></svg>
<div class="abs rule" style="top:800px"></div>
<div class="abs news-item" style="top:812px">
  <div class="img" role="img" aria-label="Box of fresh vegetables" style="background:linear-gradient(135deg,#6f9a4d,#b8432f 60%,#4c6f2f)"></div>
  <h4>Lorem Ipsum is simply dummy text of the printing and typesetting industry.</h4>
  <p>Lorem Ipsum has been the industry's standard<br>dummy text ever &nbsp;<a>... Read More</a></p>
</div>
<div class="abs rule" style="top:883px"></div>
<div class="abs news-item" style="top:895px">
  <div class="img" role="img" aria-label="Skincare product portrait" style="background:linear-gradient(135deg,#e9ddd0,#c9a58a 60%,#f2ece6)"></div>
  <h4>Lorem Ipsum is simply dummy text of the printing and typesetting industry.</h4>
  <p>Lorem Ipsum has been the industry's standard<br>dummy text ever &nbsp;<a>... Read More</a></p>
</div>
<div class="abs rule" style="top:968px"></div>

<footer class="abs footer">
  <ul style="left:68px;top:33px"><li>Home</li><li>Events</li><li>Cafe Menu</li><li>Marketplace Products</li><li>Health Info</li><li>News</li><li>Recipes</li><li>Contact Us</li></ul>
  <ul style="left:195px;top:33px"><li>Terms &amp; Conditions</li><li>Privacy Policy</li><li>Legal Notice</li></ul>
  <ul style="left:293px;top:33px"><li>Bright Leaf Office</li><li>48 Harlow Street</li><li>Lewiston, NY 14092</li><li>United States</li><li>Telephone: +1 716 555 0187</li><li>E-mail: hello@brightleafbistro.example</li></ul>
  <h5>Newsletter Sign Up</h5>
  <p class="note">Lorem Ipsum is simply dummy text of the printing and typesetting industry.</p>
  <div class="input">Enter Your E-mail Address</div>
  <div class="subscribe">Subscribe</div>
  <p class="copy">© 2015 Company Name,All Rights Reserved</p>
</footer>
</body>
</html>
```